Renewal of the Ferolanza SA Website

Ferolanza SA is a metal construction company active in industrial piping, boilermaking and metal framing. We would like to renew our site.

This website must be ready to work with Wordpress.

The site will contain the following pages: Home, skills, presentation, contact.

The site must reflect the field of the metal construction sector. It must be clear and easily understandable. The objective is not to win mandates with but to present the company and its capabilities.

I have inserted the pages of our old presentations, to describe our sector but we do not want to reuse these elements, we are waiting for your creativity to surprise us. In the 2nd phase we will complete with new images if necessary and texts

Target Market(s)

International companies in the food, chemical and pharmaceutical sectors

Industry/Entity Type

Alimentaire, pharma, chimie

Number of Pages Required

4 page

Font styles to use
Sans Serif

Colors
0054AA
0677BA
7BADD7
CADEEF
E8F1F8

Requirements
Must have
• It must contain at least the requested pages, images of illustrations, places for descriptions
Should not have
• Elements that appear or disappear, too flash,

```html
<!DOCTYPE html>
<html lang="en">
<head>
<meta charset="utf-8">
<title>Ferolanza SA – Metal Construction Company</title>
<link href="https://fonts.googleapis.com/css2?family=Oswald:wght@300;400;500;600&family=Jost:wght@400;500;600&display=swap" rel="stylesheet">
<style>
:root{
  --blue:#0054AA;
  --blue-mid:#0677BA;
  --blue-soft:#7BADD7;
  --blue-pale:#CADEEF;
  --blue-mist:#E8F1F8;
  --ink:#1f2a3a;
  --muted:#4a5566;
  --orange:#F0A20C;
  --white:#ffffff;
}
*{margin:0;padding:0;box-sizing:border-box}
html,body{width:1200px;height:3136px;overflow:hidden}
body{font-family:'Jost',sans-serif;color:var(--ink);background:var(--white);position:relative}
.abs{position:absolute}
.heading{font-family:'Oswald',sans-serif;font-weight:300;font-size:36px;color:var(--blue);text-align:center;width:1200px;left:0}
.heading b{font-weight:600}
.lead{width:1200px;left:0;text-align:center;font-size:11.5px;line-height:18px;color:var(--muted)}
.brand{font-family:'Oswald',sans-serif;font-weight:600;color:var(--blue);letter-spacing:1px;display:flex;align-items:center;gap:8px}
.brand i{display:block;width:14px;height:14px;border-radius:50%;background:var(--blue)}

/* header */
.topbar{top:0;left:0;width:1200px;height:52px;background:var(--white)}
.topbar .brand{left:156px;top:12px;font-size:24px}
.contact-chip{top:12px;display:flex;gap:10px;font-size:11px;line-height:14px}
.contact-chip .ico{width:32px;height:28px;background:var(--blue);display:flex;align-items:center;justify-content:center}
.contact-chip strong{color:var(--blue);font-weight:500;display:block}
.nav{top:52px;left:0;width:1200px;height:44px;background:var(--blue);display:flex;justify-content:center;align-items:center;gap:18px;color:var(--white);font-size:11px;text-transform:uppercase}
.nav .active{border-bottom:1px solid var(--white);padding-bottom:2px}

/* hero */
.hero{top:96px;left:0;width:1200px;height:470px;background:linear-gradient(100deg,#141a22 0%,#2c3440 35%,#34506a 60%,#1d2a38 100%)}
.hero-cut{top:496px;left:0;width:1200px;height:110px}
.hero-eyebrow{left:156px;top:198px;font-family:'Oswald',sans-serif;font-weight:300;font-size:26px;color:var(--white)}
.hero-title{left:156px;font-family:'Oswald',sans-serif;font-weight:500;color:var(--white);line-height:1}
.hero-title span{color:var(--blue-soft)}
.hero-text{left:156px;top:346px;width:360px;font-size:11px;line-height:18px;color:var(--white)}
.btn{display:flex;align-items:center;justify-content:center;background:var(--blue);color:var(--white);font-weight:600;font-size:14px}
.hero .btn{}

/* skills */
.skill-card{top:757px;width:284px;height:343px;background:var(--white);box-shadow:0 2px 12px rgba(0,0,0,.14)}
.skill-photo{width:284px;height:210px}
.skill-label{position:absolute;top:240px;left:0;width:284px;display:flex;align-items:center;justify-content:center;gap:22px;font-family:'Oswald',sans-serif;font-weight:500;font-size:15px;color:var(--blue);line-height:22px}

/* presentation */
.presentation{top:1168px;left:0;width:1200px;height:762px;background:var(--blue-mist)}
.tile{}

/* contact */
.contact{top:1930px;left:0;width:1200px;height:492px;background:linear-gradient(180deg,#0a6bb0 0%,#0f6aa8 50%,#0c62a2 100%)}
.field{background:var(--white);font-size:10px;color:#666;padding:14px 17px}
.submit{background:var(--orange);color:var(--white);font-weight:600;font-size:14px;display:flex;align-items:center;justify-content:center}

/* partners */
.partners{top:2555px;left:156px;width:890px;display:flex;justify-content:space-between}
.partner{width:60px;text-align:center;color:#c4c8ce;font-size:13px}
.partner .mark{width:44px;height:44px;margin:0 auto 4px;background:#d6d9de}

/* footer */
.footer{top:2696px;left:0;width:1200px;height:440px}
.foot-col h4{font-family:'Oswald',sans-serif;font-weight:500;font-size:15px;color:var(--white);margin-bottom:14px}
.foot-col{color:var(--white);font-size:11px;line-height:18px}
.foot-col li{list-style:none;margin-bottom:6px}
.copyright{top:3096px;left:0;width:1200px;text-align:center;color:var(--white);font-size:10px}
</style>
</head>
<body>

<!-- header -->
<div class="abs topbar">
  <div class="abs brand"><i></i>FEROLANZA SA</div>
  <div class="abs contact-chip" style="left:625px">
    <div class="ico"><svg width="14" height="16" viewBox="0 0 14 16"><path d="M7 0a6 6 0 0 0-6 6c0 4.5 6 10 6 10s6-5.5 6-10a6 6 0 0 0-6-6z" fill="#fff"/><circle cx="7" cy="6" r="2.2" fill="#0054AA"/></svg></div>
    <div><strong>Address:</strong>Rue des Forges 21, 1950 Sion, Switzerland</div>
  </div>
  <div class="abs contact-chip" style="left:913px">
    <div class="ico"><svg width="14" height="14" viewBox="0 0 24 24"><path d="M6.6 10.8a15 15 0 0 0 6.6 6.6l2.2-2.2c.3-.3.7-.4 1-.2 1.1.4 2.3.6 3.6.6.6 0 1 .4 1 1V20c0 .6-.4 1-1 1A17 17 0 0 1 3 4c0-.6.4-1 1-1h3.5c.6 0 1 .4 1 1 0 1.3.2 2.5.6 3.6.1.3 0 .7-.2 1z" fill="#fff"/></svg></div>
    <div><strong>Phone:</strong>+41 27 555 01 42</div>
  </div>
</div>
<nav class="abs nav">
  <span class="active">Home</span><span>|</span><span>Skills</span><span>|</span><span>Presentation</span><span>|</span><span>Contact</span>
</nav>

<!-- hero -->
<div class="abs hero" role="img" aria-label="Industrial plant interior with large steel pipelines and pumps"></div>
<svg class="abs hero-cut" viewBox="0 0 1200 110" width="1200" height="110">
  <polygon points="0,70 1200,2 1200,40 0,110" fill="#CADEEF"/>
  <polygon points="0,110 1200,40 1200,110" fill="#fff"/>
</svg>
<div class="abs hero-eyebrow">Ferolanza Sa</div>
<div class="abs hero-title" style="top:238px;font-size:38px">METAL <span>CONSTRU</span></div>
<div class="abs hero-title" style="top:284px;font-size:54px"><span>CTION</span> COMPANY</div>
<p class="abs hero-text">Lorem ipsum dolor sit amet, consectetur adipiscing elit, sed do eiusmod tempor incididunt ut labore et dolore magna aliqua.</p>
<div class="abs btn" style="left:156px;top:396px;width:120px;height:33px">Contact Us</div>

<!-- skills -->
<h2 class="abs heading" style="top:622px">Our <b>Skills</b></h2>
<p class="abs lead" style="top:679px">Lorem ipsum dolor sit amet, consectetur adipiscing elit, sed do eiusmod tempor incididunt ut labore et<br>dolore magna aliqua. Quis ipsum suspendisse ultrices gravida.</p>

<div class="abs skill-card" style="left:156px">
  <div class="skill-photo" role="img" aria-label="Industrial piping installation with yellow stairways" style="background:linear-gradient(135deg,#3d5d8c,#8a97a8 55%,#c9b24a)"></div>
  <svg class="abs" style="top:175px;left:0" width="284" height="40"><polygon points="0,10 284,35 284,40 0,40" fill="#CADEEF"/><polygon points="0,40 284,35 284,40" fill="#fff"/></svg>
  <div class="skill-label">
    <svg width="52" height="52" viewBox="0 0 52 52" fill="none" stroke="#1f2a3a" stroke-width="2"><path d="M2 10h20v14h18M2 18h12v14h30M40 6v28M48 22v24M14 40h34"/><rect x="36" y="4" width="8" height="6" fill="#7BADD7"/><rect x="36" y="30" width="8" height="6" fill="#7BADD7"/></svg>
    <span>LoremIndustrial<br>Piping</span>
  </div>
</div>
<div class="abs skill-card" style="left:458px">
  <div class="skill-photo" role="img" aria-label="Engineer working beside a large industrial boiler" style="background:linear-gradient(135deg,#5a4036,#7e6f66 45%,#3f4750)"></div>
  <svg class="abs" style="top:175px;left:0" width="284" height="40"><polygon points="0,20 284,35 284,40 0,40" fill="#fff"/></svg>
  <div class="skill-label">
    <svg width="52" height="52" viewBox="0 0 52 52" fill="none" stroke="#1f2a3a" stroke-width="2"><rect x="6" y="14" width="18" height="30" rx="3"/><rect x="28" y="14" width="18" height="30" rx="3"/><rect x="10" y="30" width="10" height="8" fill="#7BADD7"/><rect x="32" y="30" width="10" height="8" fill="#7BADD7"/><path d="M15 14V6M37 14V6M8 48h36"/></svg>
    <span>Boiler Making</span>
  </div>
</div>
<div class="abs skill-card" style="left:761px">
  <div class="skill-photo" role="img" aria-label="Stacked square steel profiles in a warehouse" style="background:linear-gradient(135deg,#6b3a22,#8f8f95 45%,#c3c7cc)"></div>
  <svg class="abs" style="top:175px;left:0" width="284" height="40"><polygon points="0,15 284,35 284,40 0,40" fill="#CADEEF"/><polygon points="0,40 284,35 284,40" fill="#fff"/></svg>
  <div class="skill-label">
    <svg width="52" height="52" viewBox="0 0 52 52" fill="none" stroke="#1f2a3a" stroke-width="2"><path d="M8 48V10h36v38M16 48V18h20v30M8 10l8 8M44 10l-8 8"/><rect x="6" y="6" width="40" height="4" fill="#7BADD7"/></svg>
    <span>Metal Framing</span>
  </div>
</div>

<!-- presentation -->
<section class="abs presentation"></section>
<h2 class="abs heading" style="top:1228px">Our <b>Presentation</b></h2>
<p class="abs lead" style="top:1285px">Lorem ipsum dolor sit amet, consectetur adipiscing elit, sed do eiusmod tempor incididunt ut labore et<br>dolore magna aliqua. Quis ipsum suspendisse ultrices gravida.</p>
<div class="abs tile" role="img" aria-label="Bundle of stainless steel tubes in a warehouse" style="left:156px;top:1364px;width:379px;height:400px;background:linear-gradient(135deg,#3b4450,#8fa6c0 50%,#d9e2ec)"></div>
<div class="abs tile" role="img" aria-label="Industrial plant hall with green tanks" style="left:548px;top:1364px;width:240px;height:193px;background:linear-gradient(135deg,#7aa597,#c8cfc4 50%,#4f6a66)"></div>
<div class="abs tile" role="img" aria-label="Worker assembling heavy machinery" style="left:803px;top:1364px;width:240px;height:193px;background:linear-gradient(135deg,#3a3436,#b46860 50%,#2d2a2c)"></div>
<div class="abs tile" role="img" aria-label="Long production hall with piping" style="left:548px;top:1571px;width:240px;height:193px;background:linear-gradient(135deg,#2f3a48,#a86b4e 50%,#3b3f46)"></div>
<div class="abs tile" role="img" aria-label="Technician in hard hat inspecting valves" style="left:803px;top:1571px;width:240px;height:193px;background:linear-gradient(135deg,#25406e,#d3c468 45%,#9aa3ad)"></div>
<div class="abs btn" style="left:540px;top:1825px;width:120px;height:36px">View All</div>

<!-- contact -->
<section class="abs contact" role="img" aria-label="Blue-tinted warehouse of steel profiles"></section>
<h2 class="abs heading" style="top:1989px;color:var(--white)">Contact <b>Us</b></h2>
<div class="abs field" style="left:156px;top:2074px;width:435px;height:43px">Fast Name:</div>
<div class="abs field" style="left:609px;top:2074px;width:435px;height:43px">Last Name:</div>
<div class="abs field" style="left:156px;top:2132px;width:435px;height:43px">Email:</div>
<div class="abs field" style="left:609px;top:2132px;width:435px;height:43px">Phone:</div>
<div class="abs field" style="left:156px;top:2193px;width:888px;height:104px">Message:</div>
<div class="abs submit" style="left:540px;top:2316px;width:120px;height:36px">Submit Now</div>

<!-- partners -->
<h2 class="abs heading" style="top:2480px">Our <b>Patnars</b></h2>
<div class="abs partners">
  <div class="partner"><div class="mark" style="border-radius:50%"></div>Company</div>
  <div class="partner"><div class="mark" style="border-radius:0 0 22px 22px"></div>Company</div>
  <div class="partner"><div class="mark" style="clip-path:polygon(10% 0,100% 50%,10% 100%)"></div>Company</div>
  <div class="partner"><div class="mark" style="height:24px;margin-top:10px;margin-bottom:14px;border-radius:12px"></div>Company</div>
  <div class="partner"><div class="mark" style="border-radius:50%"></div>Company</div>
  <div class="partner"><div class="mark" style="border-radius:8px"></div>Company</div>
  <div class="partner"><div class="mark" style="border-radius:50% 10% 50% 10%"></div>Company</div>
  <div class="partner"><div class="mark" style="clip-path:polygon(50% 0,100% 100%,0 100%)"></div>Company</div>
  <div class="partner"><div class="mark" style="width:30px;border-radius:50% 50% 50% 50%/60% 60% 40% 40%"></div>Company</div>
  <div class="partner"><div class="mark" style="height:14px;margin-top:14px;margin-bottom:20px;border-radius:14px 14px 0 0"></div>Company</div>
</div>

<!-- footer -->
<svg class="abs footer" viewBox="0 0 1200 440" width="1200" height="440">
  <polygon points="0,80 1200,0 1200,40 0,115" fill="#CADEEF"/>
  <polygon points="0,115 1050,25 1200,0 1200,440 0,440" fill="#0054AA"/>
  <line x1="0" y1="386" x2="1200" y2="386" stroke="#2a6fbb" stroke-width="1"/>
</svg>
<div class="abs brand" style="left:156px;top:2923px;width:209px;height:50px;background:var(--white);justify-content:center;font-size:22px"><i></i>FEROLANZA SA</div>
<div class="abs foot-col" style="left:439px;top:2868px">
  <h4>QUICK LINKS</h4>
  <ul><li>Home</li><li>Skills</li><li>Presentation</li><li>Contact</li></ul>
</div>
<div class="abs foot-col" style="left:615px;top:2868px;width:170px">
  <h4>CONTACT INFO</h4>
  <strong>Address:</strong><br>Rue des Forges 21, 1950 Sion, Switzerland<br><br>
  <strong>Phone:</strong><br>+41 27 555 01 42
</div>
<div class="abs foot-col" style="left:817px;top:2868px;width:226px">
  <h4>NEWSLETTER</h4>
  It is a long established fact that a<br>reader will
</div>
<div class="abs field" style="left:817px;top:2945px;width:190px;height:34px;padding:11px 8px;font-size:9px">Your Email Id:</div>
<div class="abs" style="left:1007px;top:2945px;width:37px;height:34px;background:#1a73e8;display:flex;align-items:center;justify-content:center">
  <svg width="16" height="16" viewBox="0 0 24 24"><path d="M2 11 22 2l-7 20-4-8z" fill="#fff"/></svg>
</div>
<div class="abs copyright">Copyright © 2023 Ferolanza SA | Designed &amp; Developed</div>

</body>
</html>
```